Business Card

I need a cool business card for Wrenvale Films. You created logo for me so I'm thinking of using you for my business card. I want something simple, clean, artsy, but yet catchy to eye. I was thinking logo on one side and the information on the other. On teh phone, web, email, fb, and vimeo it would be cool to have the icons to identify each one. I would need these business cards formatted for nimbo press. If you have any recommendations for the card I'm fine with that. I might have to much information not sure.

Logo on one side

Doran Pelk
Owner/Film Director
phone: 412.555.0142
web: wrenvalefilms.com
email: doran@wrenvalefilms.com
FB: friendspace.example/wrenvalefilmsNW
Vimeo: clipvault.example/user51930264

The other design I need is:
Milo Hartwell
Film Director/Editing
phone: 412.555.0187
web: wrenvalefilms.com
email: milo@wrenvalefilms.com

Thanks

```html
<!DOCTYPE html>
<html lang="en">
<head>
<meta charset="utf-8">
<title>Wrenvale Films – Business Card</title>
<link rel="stylesheet" href="https://fonts.googleapis.com/css2?family=Mulish:wght@400;600;800&display=swap">
<style>
  :root {
    --backdrop: #8f8a84;
    --card-dark: #1e1c1d;
    --card-light: #ffffff;
    --brand-red: #d81e2c;
    --brand-red-faint: #f6d3d7;
    --ink: #1a1a1a;
    --ink-soft: #333333;
    --wordmark-light: #e9e9e9;
  }
  * { box-sizing: border-box; margin: 0; padding: 0; }
  html, body {
    width: 1200px; height: 871px; overflow: hidden;
    background: var(--backdrop);
    font-family: "Mulish", "Century Gothic", sans-serif;
  }
  .stage { position: relative; width: 1200px; height: 871px; }
  .card {
    position: absolute; width: 560px; height: 320px;
    box-shadow: 0 14px 30px rgba(0,0,0,.35);
    overflow: hidden;
  }
  .card--front { left: 110px; top: 90px; background: var(--card-dark); }
  .card--back { left: 530px; top: 460px; background: var(--card-light); }

  .brand {
    position: absolute; display: flex; align-items: center; gap: 12px;
    font-weight: 600; letter-spacing: -0.5px;
  }
  .brand__dot { border-radius: 50%; background: var(--brand-red); flex: none; }
  .card--front .brand {
    left: 50%; top: 50%; transform: translate(-50%, -50%);
    font-size: 46px; color: var(--wordmark-light); white-space: nowrap;
  }
  .card--front .brand__dot { width: 34px; height: 34px; }
  .card--back .brand {
    left: 32px; top: 98px; font-size: 30px; color: var(--ink); white-space: nowrap;
  }
  .card--back .brand__dot { width: 24px; height: 24px; }

  .backdrop-circle {
    position: absolute; left: 170px; top: 20px; width: 250px; height: 250px;
    border-radius: 50%; border: 34px solid var(--brand-red-faint); opacity: .7;
  }

  .person { position: absolute; right: 30px; top: 112px; text-align: right; }
  .person__name { font-weight: 800; font-size: 19px; color: var(--ink); }
  .person__role { font-size: 13px; color: var(--ink-soft); margin-top: 4px; }

  .contact {
    position: absolute; right: 30px; top: 190px; list-style: none;
    font-size: 12.5px; color: var(--ink-soft);
  }
  .contact__item {
    display: flex; justify-content: flex-end; align-items: center;
    gap: 22px; height: 21px;
  }
  .contact__icon { width: 12px; height: 12px; flex: none; }
  .contact__icon--mark { border-radius: 50%; background: var(--brand-red); width: 9px; height: 9px; margin: 0 1.5px; }
</style>
</head>
<body>
<main class="stage">
  <section class="card card--front" aria-label="Card front">
    <div class="brand"><span class="brand__dot"></span>Wrenvale Films</div>
  </section>

  <section class="card card--back" aria-label="Card back">
    <div class="backdrop-circle" aria-hidden="true"></div>
    <div class="brand"><span class="brand__dot"></span>Wrenvale Films</div>

    <div class="person">
      <p class="person__name">Doran Pelk</p>
      <p class="person__role">Owner/Film Director</p>
    </div>

    <ul class="contact">
      <li class="contact__item">412.555.0142
        <svg class="contact__icon" viewBox="0 0 12 12" aria-label="phone"><path d="M2 1.5h2.2l1 2.6-1.3.9a6 6 0 0 0 3.1 3.1l.9-1.3 2.6 1V10c0 .6-.5 1-1 1A9 9 0 0 1 1 2.5c0-.5.4-1 1-1z" fill="var(--brand-red)"/></svg>
      </li>
      <li class="contact__item">doran@wrenvalefilms.com
        <svg class="contact__icon" viewBox="0 0 12 12" aria-label="email"><rect x="1" y="2.5" width="10" height="7" fill="none" stroke="var(--brand-red)" stroke-width="1.3"/><path d="M1 2.5l5 4 5-4" fill="none" stroke="var(--brand-red)" stroke-width="1.3"/></svg>
      </li>
      <li class="contact__item">wrenvalefilms.com
        <svg class="contact__icon" viewBox="0 0 12 12" aria-label="website"><circle cx="6" cy="6" r="4.8" fill="none" stroke="var(--brand-red)" stroke-width="1.2"/><path d="M1.2 6h9.6M6 1.2c-2.4 2.8-2.4 6.8 0 9.6M6 1.2c2.4 2.8 2.4 6.8 0 9.6" fill="none" stroke="var(--brand-red)" stroke-width="1"/></svg>
      </li>
      <li class="contact__item">friendspace.example/wrenvalefilmsNW
        <span class="contact__icon contact__icon--mark" aria-label="social page"></span>
      </li>
      <li class="contact__item">clipvault.example/user51930264
        <span class="contact__icon contact__icon--mark" aria-label="video channel"></span>
      </li>
    </ul>
  </section>
</main>
</body>
</html>
```